A fantastic website for a physio

We are looking for an eye catching website which can attract as many customer as possible.
We have logo designed and ready to be used in the website.
Please use the green and blue which is used in our logo for the preferred colors.
The following are the designs that I Iike:
http://www.bendwellclinic.com.au/
http://www.tullowayrehab.com.au/
We will be having other services including massage therapy, Psychology and podiatrist. You can find information about podiatry in our condition sheet.
for the address you can put Shop 7/482 Castellan Road, Dunmore Vale. It might change but for now you can leave it until I confirm that in the next couple of days.

Logo file can be downloaded here:
https://www.filecrate.example/s/qz4mpl82kvhrtx/Logo1511.jpg?dl=0

Target Market(s)

Infant to old people.
We speak Farsi.

Industry/Entity Type

Physical Therapy

Number of Pages Required

5+ page

Font styles to use
Serif

Colors
33a6d7
abd037
e667a6

Requirements
Must have
• Home, About , our services, Conditions we treat and contact
• For home page and contacts we would like a tab that can connect to another website(bookvora) for online booking. We would like the patient's to be able to leave us massage or leave their email for monthly news letter. For the condition we treat you can use the condition sheets I have attached. For about us and home page you can use brochure I have attached.
• The other things should have include: in-line contact form, Google Map, clinic hours, newsletter sign-up etc, schema rich contact information
• Social media connection to our Facebook, Instagram and linked in
Nice to have
• Search engine optimization for Merrylands and Parramatta physiotherapy.
• We can speak English and Farsi. So is nice to have an information tab for Farsi speaking people. I can provide you with the texts.

```html
<!DOCTYPE html>
<html lang="en">
<head>
<meta charset="utf-8">
<title>Linkwell Physiotherapy</title>
<link href="https://fonts.googleapis.com/css2?family=Arimo:wght@400;700&display=swap" rel="stylesheet">
<style>
  :root {
    --brand-blue: #33a6d7;
    --brand-green: #abd037;
    --nav-blue: rgba(51, 166, 215, 0.92);
    --nav-active: #2b3b42;
    --ink: #222;
    --rule: #e3e3e3;
    --hero-top: #cbb49c;
    --hero-mid: #d9c3aa;
    --hero-low: #b99e84;
  }
  * { box-sizing: border-box; margin: 0; padding: 0; }
  html, body { width: 1200px; height: 1183px; overflow: hidden; background: #fff; }
  body { font-family: "Arimo", Helvetica, Arial, sans-serif; color: var(--ink); position: relative; }

  .site-nav {
    position: absolute; top: 0; left: 0; width: 1200px; height: 45px;
    background: var(--nav-blue); z-index: 5;
    font-size: 11.5px; font-weight: 700; letter-spacing: 3px; text-transform: uppercase; color: #fff;
  }
  .site-nav a { position: absolute; top: 0; height: 45px; line-height: 41px; color: #fff; text-decoration: none; }
  .site-nav .is-active { background: var(--nav-active); color: var(--brand-green); padding: 0 16px; left: 23px; }
  .site-nav .caret { display: inline-block; margin-left: 8px; border: 4px solid transparent; border-top-color: #fff; border-bottom: 0; vertical-align: middle; }

  .hero {
    position: absolute; top: 0; left: 0; width: 1200px; height: 401px; overflow: hidden;
    background: linear-gradient(180deg, var(--hero-top) 0%, var(--hero-mid) 50%, var(--hero-low) 100%);
  }
  .hero-arrow { position: absolute; top: 50px; }
  .hero-caption { position: absolute; top: 288px; left: 0; width: 1200px; text-align: center; color: #fff; text-shadow: 0 1px 3px rgba(0,0,0,.6); }
  .hero-caption h2 { font-size: 24px; font-weight: 700; letter-spacing: -0.5px; }
  .hero-caption p { font-size: 14px; font-weight: 700; margin-top: 11px; letter-spacing: -0.3px; }
  .hero-dots { position: absolute; top: 355px; left: 575px; display: flex; gap: 5px; align-items: center; }
  .hero-dots span { width: 10px; height: 10px; border: 1px solid #fff; border-radius: 50%; }
  .hero-dots .current { width: 12px; height: 12px; background: #fff; }

  .content { position: absolute; left: 151px; width: 904px; }
  .section-title { color: var(--brand-blue); text-align: center; font-weight: 700; text-transform: uppercase; letter-spacing: -0.3px; }
  .rule { border: 0; border-top: 1px solid var(--rule); }
  .body-copy { font-size: 13.8px; line-height: 19.5px; text-align: justify; }

  .btn-contact {
    position: absolute; left: 537px; top: 825px; width: 131px; height: 44px;
    border: 1px solid #ccc; border-radius: 4px; background: #fff; text-decoration: none;
    font: 400 17px "Arimo", Helvetica, sans-serif; color: #333; line-height: 42px; text-align: center;
  }
  .brand-mark { position: absolute; top: 990px; left: 0; width: 1200px; display: flex; justify-content: center; align-items: center; gap: 12px; }
  .brand-mark .dot { width: 34px; height: 34px; border-radius: 50%; background: var(--brand-blue); }
  .brand-mark .name { font-size: 26px; font-weight: 700; color: var(--brand-blue); }
  .footer-fade { position: absolute; bottom: 0; left: 0; width: 1200px; height: 10px; background: linear-gradient(180deg, #fff, #eee); }
</style>
</head>
<body>
  <nav class="site-nav">
    <a class="is-active" href="#">Home</a>
    <a href="#" style="left:114px">About</a>
    <a href="#" style="left:199px">Our Services</a>
    <a href="#" style="left:352px">Contact</a>
    <a href="#" style="left:457px">Conditions We Treat<span class="caret"></span></a>
    <a href="#" style="left:697px" aria-label="Search">
      <svg width="12" height="12" viewBox="0 0 12 12" style="vertical-align:middle"><circle cx="5" cy="5" r="3.5" fill="none" stroke="#fff" stroke-width="1.6"/><line x1="7.6" y1="7.6" x2="10.5" y2="10.5" stroke="#fff" stroke-width="1.8"/></svg>
    </a>
    <a href="#" style="left:1046px">English</a>
    <a href="#" style="left:1148px">Farsi</a>
  </nav>

  <section class="hero" role="img" aria-label="Photo of a physiotherapist guiding a patient through a leg exercise on a blue mat">
    <svg class="hero-arrow" style="left:78px" width="22" height="30" viewBox="0 0 22 30"><polyline points="17,3 5,15 17,27" fill="none" stroke="rgba(255,255,255,.8)" stroke-width="5"/></svg>
    <svg class="hero-arrow" style="left:1106px" width="22" height="30" viewBox="0 0 22 30"><polyline points="5,3 17,15 5,27" fill="none" stroke="rgba(255,255,255,.8)" stroke-width="5"/></svg>
    <div class="hero-caption">
      <h2>Physiotherapy2</h2>
      <p>Freedom of movement with less pain and stiffness</p>
    </div>
    <div class="hero-dots"><span></span><span class="current"></span><span></span><span></span></div>
  </section>

  <div class="content" style="top:448px">
    <h1 class="section-title" style="font-size:35px">About Linkwell Physiotherapy</h1>
  </div>
  <hr class="rule content" style="top:506px">
  <p class="content body-copy" style="top:527px">We are an outpatient rehabilitation centre staffed with physical therapists, massage therapists, and an athletic trainer. We believe that during rehabilitation, the patient should be educated by their therapist in order to be able to maintain maximum exibility and pain-free living long after our work ends. Our therapists have successfully worked with all types of injuries and we work on patients of any age. We have specialized programs for youth athletics as well as pregnancy.</p>

  <div class="content" style="top:673px">
    <h2 class="section-title" style="font-size:23px">What is Physiotherapy?</h2>
  </div>
  <hr class="rule content" style="top:716px">
  <p class="content body-copy" style="top:737px">Physiotherapy is a clinical health science and profession that aims to rehabilitate and improve people with movement disorders and pain by using evidence-based and natural methods such as manual therapy, exercise, education, motivation and specialised equipment. Physiotherapy Health Solutions are a defined pathway of clinical excellence and progression of treatment. These streams of rehabilitation are: <strong>Treatment, Fitness, Stability, Health.</strong></p>

  <a class="btn-contact" href="#">Get in Touch</a>

  <div class="brand-mark"><span class="dot"></span><span class="name">Linkwell Physiotherapy</span></div>

  <div class="content" style="top:1126px">
    <h2 class="section-title" style="font-size:23px">Our Values</h2>
  </div>
  <hr class="rule content" style="top:1169px">
  <div class="footer-fade"></div>
</body>
</html>
```